Talvora Cellars WIX website

We are opening a new winery called Talvora Cellars. We think that "Wine should be an experience..." To aid in that experience, each bottle of wine label will have a unique QR code that directs patrons to a page on the site that highlights the wines. On this page each wine bottle will be displayed, the winemaking notes will be included. Also included will be food pairings with recipes, movie and music ideas and anything else that will add to the experience. I need a website that helps showcase annual wines, has a members only area (for the wine club) and allows people to purchase wine on-line. I've started the beginning of a site on WIX - talvoracellars-demo.com. There's no requirement or expectation to simply finish what I've started. I just needed to get something up and live. Let your imagination take over. I want to unique site and kicks a*s...
Updates

Logo font is Trajan Pro...

I'm open to any designs, meaning don't feel like you have to complete what I started.

I want to keep the logo and the font, however...

Other fonts used should compliment Trajan Pro.

Font styles to use
Serif
Other font styles liked:
• Trajan Pro is what was used for the logo

Requirements
Must have
• Attractive and compelling home page, red wine section, white wine section, members only area, page that speaks of and allows purchase into a wine club, all easy enough for me to edit and add pages without coding knowledge. Adding pages is why I chose WIX as the platform. Here is a list of the pages or tabs: About, Events, Vintner’s Circle, Press/Accolades, Wines - Red/White/Dessert/Summer Series (as sub pages), Contact

```html
<!DOCTYPE html>
<html lang="en">
<head>
<meta charset="utf-8">
<title>Talvora Cellars</title>
<link href="https://fonts.googleapis.com/css2?family=Cinzel:wght@400;500;600&family=Crimson+Text:ital,wght@0,400;0,600;1,400&display=swap" rel="stylesheet">
<style>
:root{
  --ink:#111111;
  --text:#333333;
  --muted:#555555;
  --orange:#e8740f;
  --white:#ffffff;
  --card:#f1f4f7;
  --frame:#dde3ea;
  --dark:#15181b;
  --footer:#181b12;
  --line:#5b5e52;
  --field-border:#8b8d82;
}
*{margin:0;padding:0;box-sizing:border-box}
html,body{width:1200px;height:5272px;overflow:hidden}
body{position:relative;background:var(--white);font-family:"Crimson Text",Georgia,serif;color:var(--text)}
.abs{position:absolute}
.display{font-family:"Cinzel","Times New Roman",serif;color:var(--ink);font-weight:500;letter-spacing:0.5px;line-height:1;white-space:nowrap}
.eyebrow{font-size:22px;color:var(--ink);line-height:1}
.center{left:0;width:1200px;text-align:center}
.btn-dark{background:var(--ink);color:var(--white);font-family:"Cinzel",serif;font-size:13px;font-weight:600;letter-spacing:2px;border-radius:20px;display:flex;align-items:center;justify-content:center}
.btn-orange{background:var(--orange);color:var(--white);font-family:"Cinzel",serif;font-size:13px;font-weight:600;letter-spacing:2px;border-radius:20px;display:flex;align-items:center;justify-content:center}

/* header */
.brand-mark{font-family:"Cinzel",serif;font-weight:500;color:var(--ink);text-align:center;line-height:1.05}
.nav a{position:absolute;top:68px;font-size:15px;color:var(--ink);text-decoration:none;white-space:nowrap}
.nav a.active{color:var(--orange)}

/* wine cards */
.product{background:var(--card)}
.product .frame{position:absolute;left:14px;right:14px;top:14px;bottom:14px;border:1px solid var(--frame)}
.product .bottle{position:absolute;left:50%;transform:translateX(-50%);top:45px;width:66px;height:240px;border-radius:14px 14px 8px 8px}
.wine-name{font-family:"Cinzel",serif;font-size:18px;color:var(--ink);text-align:center;width:258px}
.wine-desc{font-size:16px;font-style:italic;color:var(--muted);text-align:center;width:258px}
.wine-more{font-family:"Cinzel",serif;font-size:10px;letter-spacing:1.5px;color:var(--muted);text-align:center;width:258px}
.arrow{width:32px;height:30px;border:1px solid #cfcfcf;border-radius:4px;display:flex;align-items:center;justify-content:center}

/* feature tiles */
.tile-label{font-family:"Cinzel",serif;font-size:28px;color:var(--white);letter-spacing:1.5px}

/* footer */
.field{border:1px solid var(--field-border);border-radius:22px;color:#cfcfc6;font-size:13px;padding-left:18px;display:flex;align-items:center}
.foot-head{font-family:"Cinzel",serif;font-size:20px;color:var(--white);letter-spacing:1px}
.foot-link{font-size:15px;color:#e6e6e0}
.social{width:33px;height:33px;background:#7a2a3c;border-radius:3px}
</style>
</head>
<body>

<header>
  <div class="abs brand-mark" style="left:58px;top:34px;width:124px;font-size:24px;">TALVORA<br><span style="font-size:13px;letter-spacing:4px">CELLARS</span></div>
  <div class="abs" style="left:940px;top:19px;font-size:13px;color:var(--ink)">My Account</div>
  <div class="abs btn-dark" style="left:1030px;top:10px;width:103px;height:35px;font-family:'Crimson Text',serif;font-size:15px;letter-spacing:0;font-weight:400">Login</div>
  <nav class="nav">
    <a class="active" style="left:512px">Home</a>
    <a style="left:595px">About</a>
    <a style="left:680px">Events</a>
    <a style="left:766px">Vintner’s Circle</a>
    <a style="left:900px">Press</a>
    <a style="left:982px">Wine</a>
    <a style="left:1060px">Contact Us</a>
  </nav>
</header>

<section>
  <div class="abs eyebrow" style="left:72px;top:240px">Because wine</div>
  <h1 class="abs display" style="left:72px;top:282px;font-size:41px;line-height:58px;font-weight:500;letter-spacing:0">SHOULD BE<br>AN EXPERIENCE...</h1>
  <p class="abs" style="left:68px;top:403px;width:410px;font-size:17px;line-height:26px;color:var(--ink)">We are currently making and aging wines for a future launch.&nbsp; Please check back.</p>
  <div class="abs btn-dark" style="left:68px;top:479px;width:165px;height:37px">VIEW DETAILS</div>
  <div class="abs" role="img" aria-label="Red and white wine bottles in front of a large winery crest" style="left:545px;top:100px;width:585px;height:510px;border-radius:8px;background:radial-gradient(ellipse at 50% 45%,#e8e8e8 0%,#cfcfcf 55%,#f4f4f4 100%)"></div>
</section>

<section>
  <div class="abs" role="img" aria-label="Tasting room bar with brick walls and shelves of wine" style="left:68px;top:729px;width:573px;height:420px;background:linear-gradient(135deg,#6b3e28 0%,#3a2418 55%,#8a6a4c 100%)"></div>
  <div class="abs eyebrow" style="left:680px;top:746px">Introducing</div>
  <h2 class="abs display" style="left:680px;top:787px;font-size:42px">TALVORA CELLARS</h2>
  <p class="abs" style="left:680px;top:862px;width:455px;font-size:17px;line-height:26.8px;color:var(--text)">Temporibus autem quibusdam et aut officiis debitis aut rerum necessitatibus saepe eveniet ut et voluptates repudiandae sint et molestiae non recusandae. Itaque earum rerum hic tenetur a sapiente delectus, ut aut reiciendis voluptatibus maiores alias consequatur aut perferendis doloribus asperiores repellat. The wise man therefore always holds in these matters...</p>
  <div class="abs btn-dark" style="left:680px;top:1092px;width:145px;height:36px">READ MORE</div>
</section>

<section>
  <div class="abs eyebrow center" style="top:1252px">Annual Wines</div>
  <h2 class="abs display center" style="top:1292px;font-size:44px">RED WINE</h2>
  <div class="abs arrow" style="left:68px;top:1333px"><svg width="10" height="10" viewBox="0 0 10 10"><path d="M7 1 3 5l4 4" fill="none" stroke="#222" stroke-width="1.6"/></svg></div>
  <div class="abs arrow" style="left:106px;top:1333px"><svg width="10" height="10" viewBox="0 0 10 10"><path d="M3 1l4 4-4 4" fill="none" stroke="#222" stroke-width="1.6"/></svg></div>

  <div class="abs" role="img" aria-label="Wine bottle, glass and barrel on a rustic table" style="left:68px;top:1372px;width:256px;height:328px;background:linear-gradient(160deg,#5a4436 0%,#2c2420 60%,#3d3040 100%)"></div>

  <div class="abs product" style="left:336px;top:1372px;width:258px;height:328px"><div class="frame"></div><div class="bottle" role="img" aria-label="Red wine bottle" style="background:linear-gradient(180deg,#5a1a22,#3e1016)"></div></div>
  <div class="abs product" style="left:606px;top:1372px;width:258px;height:328px"><div class="frame"></div><div class="bottle" role="img" aria-label="Amber wine bottle" style="background:linear-gradient(180deg,#8a4a1c,#5a2c10)"></div></div>
  <div class="abs product" style="left:876px;top:1372px;width:258px;height:328px"><div class="frame"></div><div class="bottle" role="img" aria-label="Purple wine bottle" style="background:linear-gradient(180deg,#8a2a8e,#5a1660)"></div></div>

  <div class="abs wine-name" style="left:336px;top:1716px">QUIA VOLUPTAS</div>
  <div class="abs wine-desc" style="left:336px;top:1744px">Duis aute irure dolor in voluptate...</div>
  <div class="abs wine-more" style="left:336px;top:1776px">READ MORE</div>
  <div class="abs wine-name" style="left:606px;top:1716px">GREAT EXPLORER</div>
  <div class="abs wine-desc" style="left:606px;top:1744px">Duis aute irure dolor in voluptate...</div>
  <div class="abs wine-more" style="left:606px;top:1776px">READ MORE</div>
  <div class="abs wine-name" style="left:876px;top:1716px">ULLAM CORPORIS</div>
  <div class="abs wine-desc" style="left:876px;top:1744px">Duis aute irure dolor in voluptate...</div>
  <div class="abs wine-more" style="left:876px;top:1776px">READ MORE</div>
</section>

<section>
  <div class="abs" role="img" aria-label="Wine bottles, glasses and corks on a dark rustic backdrop" style="left:0;top:1860px;width:1200px;height:409px;background:linear-gradient(90deg,#3a2c26 0%,#6a4232 30%,#5a3a2e 50%,#6a4232 70%,#3a2c26 100%)"></div>
  <div class="abs eyebrow center" style="top:1970px;color:var(--white);font-size:25px">We Make</div>
  <h2 class="abs display center" style="top:2010px;font-size:45px;color:var(--white)">GREAT WINES...IN MONTANA.</h2>
  <p class="abs center" style="top:2070px;font-size:17px;color:var(--white)">Duis aute irure dolor in reprehenderit in voluptate velit esse cillum dolore eu fugiat nulla pariatur</p>
  <div class="abs btn-orange" style="left:528px;top:2118px;width:146px;height:37px;box-shadow:0 0 0 2px #fff inset">SHOP HERE</div>
</section>

<section>
  <div class="abs eyebrow center" style="top:2341px">Annual Wines</div>
  <h2 class="abs display center" style="top:2382px;font-size:44px">WHITE WINE</h2>
  <div class="abs arrow" style="left:1059px;top:2421px"><svg width="10" height="10" viewBox="0 0 10 10"><path d="M7 1 3 5l4 4" fill="none" stroke="#222" stroke-width="1.6"/></svg></div>
  <div class="abs arrow" style="left:1101px;top:2421px"><svg width="10" height="10" viewBox="0 0 10 10"><path d="M3 1l4 4-4 4" fill="none" stroke="#222" stroke-width="1.6"/></svg></div>

  <div class="abs product" style="left:68px;top:2464px;width:258px;height:326px"><div class="frame"></div><div class="bottle" role="img" aria-label="White wine bottle" style="background:linear-gradient(180deg,#efe0b0,#d8c080)"></div></div>
  <div class="abs product" style="left:336px;top:2464px;width:258px;height:326px"><div class="frame"></div><div class="bottle" role="img" aria-label="White wine bottle" style="background:linear-gradient(180deg,#eee6b8,#d2c88a)"></div></div>
  <div class="abs product" style="left:606px;top:2464px;width:258px;height:326px"><div class="frame"></div><div class="bottle" role="img" aria-label="Rosé wine bottle" style="background:linear-gradient(180deg,#f4d2c4,#e2a890)"></div></div>
  <div class="abs" role="img" aria-label="Guests pouring wine at an outdoor vineyard table" style="left:876px;top:2464px;width:258px;height:326px;background:linear-gradient(180deg,#6a7a58 0%,#8a8468 50%,#d8d4cc 100%)"></div>

  <div class="abs wine-name" style="left:68px;top:2807px">QUIA VOLUPTAS</div>
  <div class="abs wine-desc" style="left:68px;top:2835px">Duis aute irure dolor in voluptate...</div>
  <div class="abs wine-more" style="left:68px;top:2867px">READ MORE</div>
  <div class="abs wine-name" style="left:336px;top:2807px">GREAT EXPLORER</div>
  <div class="abs wine-desc" style="left:336px;top:2835px">Duis aute irure dolor in voluptate...</div>
  <div class="abs wine-more" style="left:336px;top:2867px">READ MORE</div>
  <div class="abs wine-name" style="left:606px;top:2807px">ULLAM CORPORIS</div>
  <div class="abs wine-desc" style="left:606px;top:2835px">Duis aute irure dolor in voluptate...</div>
  <div class="abs wine-more" style="left:606px;top:2867px">READ MORE</div>
</section>

<section>
  <div class="abs" style="left:0;top:2949px;width:1200px;height:684px;background:linear-gradient(135deg,#1c1f22,#0f1113)"></div>
  <div class="abs" role="img" aria-label="Black and white portrait of the winemaker tasting from a wine glass" style="left:68px;top:3070px;width:532px;height:397px;background:linear-gradient(90deg,#f0f0f0 0%,#9a9a9a 45%,#3a3a3a 100%)"></div>
  <div class="abs eyebrow" style="left:672px;top:3107px;color:var(--white)">A Message From</div>
  <h2 class="abs display" style="left:672px;top:3148px;font-size:44px;color:var(--white)">THE WINEMAKER</h2>
  <p class="abs" style="left:672px;top:3217px;width:465px;font-size:17px;line-height:26.5px;color:#e0e0e0">I started my winemaking journey with one simple goal in mind – I wanted to make wine as good or better than the wine I could buy.&nbsp; At the time of that goal in 2015, I had no perspective on the path that would form before me.</p>
  <p class="abs" style="left:672px;top:3337px;width:465px;font-size:17px;line-height:26.5px;color:#e0e0e0">I’m excited for you to try my wine. Pair it with the food ideas. Follow the recipes; listen to the music.</p>
  <p class="abs" style="left:674px;top:3406px;font-size:17px;color:var(--orange)">Enjoy...the experience.</p>
</section>

<section>
  <div class="abs eyebrow center" style="top:3703px">Also Included</div>
  <h2 class="abs display center" style="top:3743px;font-size:44px">EXTRA FEATURES</h2>
  <div class="abs" role="img" aria-label="Glasses of shrimp cocktail on a wooden board" style="left:68px;top:3824px;width:520px;height:497px;background:linear-gradient(160deg,#3a2c22 0%,#b86a2c 45%,#4a5a2c 100%)"></div>
  <div class="abs tile-label" style="left:68px;width:520px;text-align:center;top:4268px">FOOD PAIRINGS</div>
  <div class="abs" role="img" aria-label="Musician performing on a dark stage" style="left:612px;top:3824px;width:521px;height:237px;background:linear-gradient(135deg,#1a1e18 0%,#3a3020 50%,#a0501a 100%)"></div>
  <div class="abs tile-label" style="left:641px;top:4008px">MUSIC</div>
  <div class="abs" role="img" aria-label="Popcorn bucket and 3D glasses under blue light" style="left:612px;top:4086px;width:521px;height:235px;background:linear-gradient(135deg,#1a2a7a 0%,#2a4ad0 45%,#7a1a2a 100%)"></div>
  <div class="abs tile-label" style="left:641px;top:4268px">MOVIE</div>
</section>

<footer>
  <div class="abs" style="left:0;top:4395px;width:1200px;height:877px;background:linear-gradient(180deg,#1d2116,#14170f)"></div>
  <div class="abs" style="left:599px;top:4395px;width:1px;height:57px;background:var(--line)"></div>
  <div class="abs" style="left:68px;top:4452px;width:1065px;height:1px;background:var(--line)"></div>
  <div class="abs eyebrow center" style="top:4508px;color:var(--white)">Contact Us</div>
  <h2 class="abs display center" style="top:4550px;font-size:44px;color:var(--white)">ENGAGED WITH US</h2>

  <div class="abs field" style="left:258px;top:4635px;width:219px;height:43px">Name:</div>
  <div class="abs field" style="left:490px;top:4635px;width:219px;height:43px">Email:</div>
  <div class="abs field" style="left:721px;top:4635px;width:221px;height:43px">Phone:</div>
  <div class="abs btn-orange" style="left:258px;top:4698px;width:219px;height:43px">SUBMIT</div>
  <div class="abs field" style="left:490px;top:4698px;width:452px;height:43px">Your Message...</div>

  <div class="abs" style="left:68px;top:4803px;width:1065px;height:1px;background:var(--line)"></div>
  <div class="abs" style="left:599px;top:4803px;width:1px;height:67px;background:var(--line)"></div>

  <div class="abs brand-mark" style="left:68px;top:5010px;width:235px;font-size:40px;color:var(--white)">TALVORA<br><span style="font-size:18px;letter-spacing:8px">CELLARS</span></div>

  <div class="abs foot-head" style="left:399px;top:4913px">QUICK LINKS</div>
  <div class="abs foot-link" style="left:399px;top:4965px">Home</div>
  <div class="abs foot-link" style="left:399px;top:4998px">About</div>
  <div class="abs foot-link" style="left:399px;top:5032px">Events</div>
  <div class="abs foot-link" style="left:399px;top:5065px">Vintner’s Circle</div>
  <div class="abs foot-link" style="left:399px;top:5099px">Press</div>
  <div class="abs foot-link" style="left:399px;top:5132px">Wine</div>
  <div class="abs foot-link" style="left:399px;top:5166px">Contact Us</div>

  <div class="abs foot-head" style="left:668px;top:4913px">CONTACT US</div>
  <svg class="abs" style="left:670px;top:4985px" width="22" height="26" viewBox="0 0 22 26" aria-hidden="true"><circle cx="11" cy="11" r="10" fill="#7a2a3c"/><path d="M11 5a4 4 0 0 0-4 4c0 3 4 7 4 7s4-4 4-7a4 4 0 0 0-4-4z" fill="#fff"/><circle cx="11" cy="9" r="1.5" fill="#7a2a3c"/></svg>
  <div class="abs foot-link" style="left:704px;top:4982px;width:260px;font-size:14px;line-height:21px">18 Orchard Lane, Lorem ipsum dolor sit Hollowbrook 59MT USA</div>
  <svg class="abs" style="left:670px;top:5041px" width="22" height="22" viewBox="0 0 22 22" aria-hidden="true"><circle cx="11" cy="11" r="10" fill="#7a2a3c"/><path d="M7.5 6c.6-.6 1.4-.5 1.8.1l1 1.5c.3.5.2 1.1-.2 1.4l-.6.5c.6 1.3 1.6 2.3 2.9 2.9l.5-.6c.3-.4.9-.5 1.4-.2l1.5 1c.6.4.7 1.2.1 1.8l-.7.7c-3.3.5-8.4-4.6-7.9-7.9z" fill="#fff"/></svg>
  <div class="abs foot-link" style="left:704px;top:5042px;font-size:14px">+1 (555) 014 2270</div>
  <svg class="abs" style="left:670px;top:5099px" width="22" height="22" viewBox="0 0 22 22" aria-hidden="true"><circle cx="11" cy="11" r="10" fill="#7a2a3c"/><rect x="5.5" y="7" width="11" height="8" rx="1" fill="#fff"/><path d="M5.5 7.5 11 11.5l5.5-4" fill="none" stroke="#7a2a3c" stroke-width="1"/></svg>
  <div class="abs foot-link" style="left:704px;top:5100px;font-size:14px">info@talvoracellars-demo.com</div>

  <div class="abs foot-head" style="left:1010px;top:4913px">FOLLOW US</div>
  <div class="abs social" role="img" aria-label="Social profile link" style="left:1010px;top:4969px"></div>
  <div class="abs social" role="img" aria-label="Social profile link" style="left:1055px;top:4969px"></div>
  <div class="abs social" role="img" aria-label="Social profile link" style="left:1100px;top:4969px"></div>

  <div class="abs" style="left:68px;top:5218px;font-family:'Cinzel',serif;font-size:26px;color:var(--white);line-height:1">CASA LUNETTA</div>
  <div class="abs" style="left:68px;top:5248px;font-size:9px;letter-spacing:1px;color:#cfcfc6">VIOGNIER · MARSANNE · ROUSSANNE</div>
  <div class="abs" style="left:880px;top:5228px;width:253px;text-align:right;font-size:11px;color:#e6e6e0">© <span style="color:var(--orange)">Talvora Cellars</span>, 2024. All Rights Reserved.</div>
</footer>

</body>
</html>
```